Legal Agribusiness Capability Brochure Design

Design A4 sized 6 page Legal Agribusiness Capability Brochure. Design is to be consistent with current marketing materials - logo, letterhead, website and business card to be provided.
Cover page - Firm name and logo, Agribusiness Capability Statement heading with image 1 below
Inside cover page - About Us section with image 2 below then Awards section below image
Inside middle page - Our Expertise with image 3 below
Inside back page - Our Experience with image 4 below
Back page - Senior Lawyers with image 5 below
Outside Middle Back Page - Contact Us with image 6
Updates

To provide more details to designers for brochure

Target Market(s)

Agribusiness - Australia

Industry/Entity Type

Legal

Colors

Designer to choose colors to be used in the design.

Requirements
Must have
• Use content from uloaded file - Agribusiness Brochure Content
• Use images uploaded
• Professional appearance
• Consistent with current marketing and website https://ferngatelegal.com.au/

```html
<!DOCTYPE html>
<html lang="en">
<head>
<meta charset="utf-8">
<title>Agribusiness Capability Statement</title>
<link href="https://fonts.googleapis.com/css2?family=Oswald:wght@500&family=Roboto+Condensed:wght@400;700&family=Tinos&family=Roboto:wght@400;500&display=swap" rel="stylesheet">
<style>
:root{
  --blue:#0a86cf;
  --yellow:#fdbf12;
  --grey:#cdcfd1;
  --white:#ffffff;
  --ink:#1f1f1f;
  --muted:#5e6063;
  --pale-blue:#cfe2f5;
  --soft-blue:#8dbbe6;
}
*{margin:0;padding:0;box-sizing:border-box}
html,body{width:1200px;height:849px;overflow:hidden;background:var(--white)}
.spread{position:relative;width:1200px;height:849px;overflow:hidden;font-family:"Roboto Condensed",sans-serif}
.backdrop{position:absolute;inset:0}
.brand-row{position:absolute;top:0;height:95px;display:flex;align-items:center}
.brand-row.left{left:143px;gap:14px}
.brand-row.right{left:697px;gap:18px}
.seal{border-radius:50%;border:2px solid var(--ink);background:var(--white)}
.award{border-radius:50%;background:#f3e6bd}
.firm{display:flex;align-items:center;gap:8px}
.firm-mark{background:var(--blue);border-radius:4px}
.firm-text{display:flex;flex-direction:column;line-height:1}
.firm-name{font-family:"Roboto",sans-serif;font-weight:500;color:var(--blue);letter-spacing:.5px}
.firm-tag{font-family:"Roboto",sans-serif;color:var(--muted);margin-top:4px}
.left .firm-mark{width:34px;height:34px}
.left .firm-name{font-size:17px}
.left .firm-tag{font-size:9px}
.right .firm-mark{width:50px;height:50px}
.right .firm-name{font-size:25px}
.right .firm-tag{font-size:12px}
.contact{position:absolute;left:0;top:148px;width:600px;text-align:center;color:var(--white)}
.contact h2{font-family:"Oswald",sans-serif;font-weight:500;font-size:28px;letter-spacing:.5px;line-height:1.1}
.contact .intro{font-family:"Tinos",serif;font-size:12.5px;line-height:16px;margin-top:5px}
.office h3{font-family:"Roboto Condensed",sans-serif;font-weight:700;color:var(--yellow);font-size:13.5px;margin-top:12px}
.office p{font-size:9.5px;line-height:14px}
.office .phone{font-weight:700;font-size:11.5px;line-height:15px}
.office .web{font-weight:700}
.rule{width:179px;height:2px;background:var(--yellow);margin:5px auto 0}
.title{position:absolute;left:600px;top:186px;width:600px;text-align:center;font-family:"Tinos",serif;font-weight:400;line-height:70px;font-size:76px;text-shadow:3px 4px 6px rgba(0,0,0,.45)}
.title span{display:block;transform:scaleX(.86);transform-origin:center}
.title .l1{color:var(--white)}
.title .l2{color:var(--pale-blue)}
.title .l3{color:var(--soft-blue)}
</style>
</head>
<body>
<main class="spread">
  <svg class="backdrop" width="1200" height="849" viewBox="0 0 1200 849">
    <defs>
      <linearGradient id="harvest-sky" x1="0" y1="0" x2="1" y2="1">
        <stop offset="0" stop-color="#9c948c"/>
        <stop offset=".5" stop-color="#cfc6b9"/>
        <stop offset="1" stop-color="#b7a88f"/>
      </linearGradient>
      <linearGradient id="harvest-crop" x1="0" y1="0" x2="0" y2="1">
        <stop offset="0" stop-color="#c9a33c"/>
        <stop offset=".5" stop-color="#c79a48"/>
        <stop offset="1" stop-color="#a8762f"/>
      </linearGradient>
      <linearGradient id="pasture" x1="0" y1="0" x2="0" y2="1">
        <stop offset="0" stop-color="#d9c9a8"/>
        <stop offset=".35" stop-color="#d2b98f"/>
        <stop offset=".55" stop-color="#b88a5e"/>
        <stop offset=".75" stop-color="#a98764"/>
        <stop offset="1" stop-color="#8a553a"/>
      </linearGradient>
    </defs>
    <rect y="95" width="1200" height="405" fill="var(--yellow)"/>
    <polygon points="0,167 391,120 600,205 809,120 1200,167 1200,431 0,431" fill="var(--blue)"/>
    <polyline points="0,167 391,120" fill="none" stroke="var(--white)" stroke-width="3"/>
    <polyline points="809,120 1200,167" fill="none" stroke="var(--white)" stroke-width="3"/>
    <polygon points="332,95 868,95 600,205" fill="var(--grey)"/>
    <g role="img" aria-label="Photo of a yellow combine harvester cutting golden wheat under a cloudy sky">
      <polygon points="0,500 600,433 600,849 0,849" fill="url(#harvest-sky)"/>
      <polygon points="0,640 600,600 600,849 0,849" fill="url(#harvest-crop)"/>
    </g>
    <g role="img" aria-label="Photo of a flock of merino sheep standing in a dry red-soil paddock">
      <polygon points="600,433 1200,500 1200,849 600,849" fill="url(#pasture)"/>
    </g>
    <polyline points="0,500 600,433 1200,500" fill="none" stroke="var(--white)" stroke-width="3"/>
    <line x1="600" y1="95" x2="600" y2="849" stroke="var(--white)" stroke-width="1"/>
  </svg>

  <header class="brand-row left">
    <div class="seal" style="width:48px;height:48px"></div>
    <div class="firm">
      <div class="firm-mark"></div>
      <div class="firm-text"><span class="firm-name">FERNGATE LEGAL</span><span class="firm-tag">Commercial + Litigation</span></div>
    </div>
    <div class="award" style="width:50px;height:50px;margin-left:8px"></div>
  </header>

  <header class="brand-row right">
    <div class="seal" style="width:62px;height:62px"></div>
    <div class="firm">
      <div class="firm-mark"></div>
      <div class="firm-text"><span class="firm-name">FERNGATE LEGAL</span><span class="firm-tag">Commercial + Litigation</span></div>
    </div>
    <div class="award" style="width:66px;height:66px;margin-left:14px"></div>
  </header>

  <section class="contact">
    <h2>CONTACT US</h2>
    <p class="intro">If you have any questions or require any assistance in relation<br>to agribusiness law, please contact us at our Geraldton or Perth office.</p>
    <div class="office">
      <h3>Geraldton Office</h3>
      <p>Suite 4, Harbourview Chambers</p>
      <p>12 Saltbush Lane</p>
      <p>Geraldton WA 6530</p>
      <p class="phone">+61 8 9000 1120; + 61 8 9000 1121</p>
      <p>info@ferngatelegal.com.au</p>
    </div>
    <div class="rule"></div>
    <div class="office">
      <h3 style="margin-top:6px">Perth Office</h3>
      <p>88 Kestrel Avenue</p>
      <p>West Perth WA 6005</p>
      <p class="phone">+61 8 9000 2230; + 61 8 9000 2231</p>
      <p>info@ferngatelegal.com.au</p>
      <p class="web">https://ferngatelegal.com.au/</p>
    </div>
  </section>

  <h1 class="title">
    <span class="l1">AGRIBUSINESS</span>
    <span class="l2">CAPABILITY</span>
    <span class="l3">STATEMENT</span>
  </h1>
</main>
</body>
</html>
```